Business Card Design Project

We need a simple business card design that uses our current logo.
We need to have the current logo put into a high res format.
We need to have 1 card made with contact information.
We will supply the information for the 4 employees.
Industry/Entity Type
Business
Requirements
Must have
- The contact information is as follows:
Mark Dellweather
Producer/CEO
c. 949-555-0147
f. 650-555-0193
markd@lanternbay.example
Al Vostrand, CFO
c. 949-555-0162
f. 650-555-0193
alv@lanternbay.example
Peter Malvane, PR
c. 267-555-0128
f. 650-555-0193
pmalvane@lanternbay.example
Tim Garrowby, Producer
c. 949-555-0184
f. 650-555-0193
timg@lanternbay.example
The address for all cards is:
318 W Calle Norvento #2715, San Clemente, CA 92681

```html
<!DOCTYPE html>
<html lang="en">
<head>
<meta charset="utf-8">
<title>Business Card – Tim Garrowby</title>
<link rel="stylesheet" href="https://fonts.googleapis.com/css2?family=Open+Sans:wght@400&family=Arimo:wght@400&display=swap">
<style>
  :root {
    --card-blue: #00bfff;
    --band-blue: #2ccbff;
    --ink: #111111;
  }
  html, body {
    margin: 0;
    padding: 0;
    overflow: hidden;
  }
  .card {
    position: relative;
    width: 763px;
    height: 1200px;
    background: var(--card-blue);
    color: var(--ink);
    font-family: "Open Sans", sans-serif;
    overflow: hidden;
  }
  .identity {
    position: absolute;
    top: 222px;
    left: 0;
    width: 100%;
    text-align: center;
  }
  .identity__name {
    margin: 0;
    font-size: 46px;
    font-weight: 400;
    line-height: 1.2;
  }
  .identity__role {
    margin: 0;
    font-size: 29px;
    line-height: 1.2;
  }
  .contact-band {
    position: absolute;
    top: 453px;
    left: 0;
    width: 100%;
    height: 226px;
    background: var(--band-blue);
    text-align: center;
  }
  .contact-band__title {
    margin: 26px 0 4px;
    font-size: 43px;
    font-weight: 400;
    line-height: 1.1;
  }
  .contact-band__line {
    margin: 0;
    font-size: 27px;
    line-height: 33px;
  }
  .website {
    position: absolute;
    top: 864px;
    left: 0;
    width: 100%;
    margin: 0;
    text-align: center;
    font-size: 46px;
    line-height: 1.2;
  }
  .tagline {
    position: absolute;
    top: 1142px;
    left: 0;
    width: 100%;
    margin: 0;
    text-align: center;
    font-family: "Arimo", sans-serif;
    font-size: 15px;
  }
</style>
</head>
<body>
  <main class="card">
    <header class="identity">
      <h1 class="identity__name">Tim Garrowby</h1>
      <p class="identity__role">Producer</p>
    </header>

    <section class="contact-band">
      <h2 class="contact-band__title">Contact</h2>
      <p class="contact-band__line">C: 949-555-0184</p>
      <p class="contact-band__line">F: 650-555-0193</p>
      <p class="contact-band__line">318 W Calle Norvento #2715, San Clemente, CA 92681</p>
      <p class="contact-band__line">E: timg@lanternbay.example</p>
    </section>

    <p class="website">www.lanternbay.example</p>

    <p class="tagline">brand development | design | visual communication</p>
  </main>
</body>
</html>
```